Web Design Project - Event Management Company

A web-page design needs to be created for an event management company. The logo has already been created, the design needs to draw on the themes and colors of the logo and extend on that.

The event management company likes to differentiate itself from others by being a bit "un-conventional" and being able to think outside the box.

the specialise in corporate events, weddings, AGMs, anything that requires coordination of resources. They also can provide Audio Visual services such as recording events.

final design will also require HTML implementation

```html
<!DOCTYPE html>
<html lang="en">
<head>
<meta charset="utf-8">
<title>Odd Block Events</title>
<link rel="stylesheet" href="https://fonts.googleapis.com/css2?family=Jost:wght@300;400&family=Oswald:wght@500;600&family=Open+Sans:wght@400&family=Arimo:wght@700&display=swap">
<style>
  :root {
    --orange: #f5a036;
    --pink: #f49bb6;
    --blue: #63c4e1;
    --red: #e85d26;
    --lime: #d2d215;
    --ink: #262626;
    --text: #2e2e2e;
    --frame: #dcdcdc;
    --button: #222222;
    --link: #2a55d6;
    --page: #ffffff;
  }
  * { margin: 0; padding: 0; box-sizing: border-box; }
  html, body { width: 1200px; height: 1000px; overflow: hidden; background: var(--page); }
  .page { position: relative; width: 1200px; height: 1000px; color: var(--text); font-family: "Open Sans", Arial, sans-serif; }

  .brand { position: absolute; left: 257px; top: 118px; display: flex; align-items: center; gap: 10px; }
  .brand-mark { width: 24px; height: 24px; background: var(--orange); }
  .brand-name { font-family: "Oswald", sans-serif; font-weight: 500; font-size: 31px; color: #3c3c3c; letter-spacing: 0.5px; line-height: 1; }

  .main-nav { position: absolute; left: 551px; top: 0; display: flex; gap: 3px; }
  .nav-item { width: 76px; height: 131px; display: flex; align-items: flex-end; justify-content: center; padding-bottom: 7px;
    font-family: "Oswald", sans-serif; font-weight: 500; font-size: 15px; color: #fff; text-decoration: none; letter-spacing: 0.3px; }
  .nav-home { background: var(--orange); }
  .nav-about { background: var(--pink); }
  .nav-services { background: var(--blue); }
  .nav-gallery { background: var(--red); }
  .nav-contact { background: var(--lime); }

  .photo-frame { position: absolute; background: var(--frame); padding: 9px 9px 9px 9px; }
  .photo { width: 100%; height: 100%; }
  .frame-weddings { left: 255px; top: 180px; width: 419px; height: 261px; }
  .photo-weddings { background: linear-gradient(135deg, #2f5a1e 0%, #7fa35a 30%, #f2f2ee 48%, #9aa08f 60%, #e9ecea 75%, #5f8b3a 100%); }
  .frame-corporate { left: 508px; top: 461px; width: 437px; height: 262px; padding: 9px 10px 10px 12px; }
  .photo-corporate { background: linear-gradient(180deg, #5a2e1c 0%, #8b5a3e 30%, #b9a39a 55%, #e6e1dc 78%, #d9d3cf 100%); }

  .section-title { font-family: "Jost", sans-serif; font-weight: 300; color: var(--ink); line-height: 1; }
  .feature-text { font-size: 9.4px; line-height: 12.4px; text-align: justify; }
  .button { position: absolute; display: flex; align-items: center; justify-content: center; background: var(--button); color: #fff;
    font-family: "Arimo", Arial, sans-serif; font-weight: 700; font-size: 13px; letter-spacing: 0.3px; text-decoration: none; height: 36px; }

  .feature-weddings { position: absolute; left: 708px; top: 274px; width: 237px; }
  .feature-weddings .section-title { font-size: 35px; letter-spacing: 1px; margin-bottom: 8px; }
  .btn-gallery { left: 708px; top: 405px; width: 237px; }

  .feature-corporate { position: absolute; left: 257px; top: 521px; width: 210px; }
  .feature-corporate .section-title { font-size: 35px; line-height: 39px; margin-bottom: 6px; }
  .feature-corporate .line-wide { letter-spacing: 3px; }
  .feature-corporate .line-narrow { letter-spacing: 1px; }
  .btn-events { left: 256px; top: 688px; width: 226px; }

  .info-col { position: absolute; top: 750px; width: 173px; }
  .info-bar { height: 6px; }
  .info-col .section-title { font-size: 26px; text-align: center; margin: 16px 0 14px; letter-spacing: 0.5px; }
  .col-about { left: 282px; } .col-about .info-bar { background: var(--lime); }
  .col-services { left: 514px; } .col-services .info-bar { background: var(--pink); }
  .col-clients { left: 746px; width: 173px; } .col-clients .info-bar { background: var(--orange); }

  .footer-rule { position: absolute; left: 255px; top: 930px; display: flex; gap: 3px; }
  .footer-rule span { width: 66px; height: 2px; }
  .site-footer { position: absolute; left: 0; top: 946px; width: 1200px; text-align: center; font-size: 9px; color: #222; }
  .site-footer a { color: var(--link); text-decoration: none; }
</style>
</head>
<body>
<div class="page">
  <header>
    <div class="brand">
      <span class="brand-mark"></span>
      <span class="brand-name">ODD BLOCK EVENTS</span>
    </div>
    <nav class="main-nav">
      <a class="nav-item nav-home" href="#">HOME</a>
      <a class="nav-item nav-about" href="#">ABOUT</a>
      <a class="nav-item nav-services" href="#">SERVICES</a>
      <a class="nav-item nav-gallery" href="#">GALLERY</a>
      <a class="nav-item nav-contact" href="#">CONTACT</a>
    </nav>
  </header>

  <main>
    <div class="photo-frame frame-weddings">
      <div class="photo photo-weddings" role="img" aria-label="Outdoor wedding ceremony with white drapes and a bouquet of white flowers"></div>
    </div>
    <section class="feature-weddings">
      <h2 class="section-title">WEDDINGS</h2>
      <p class="feature-text">Lorem Ipsum is simply dummy text of the printing and typesetting industry. Lorem Ipsum has been the industry's standard dummy text ever since the 1500s, when an unknown printer took a galley of type and scrambled it to make a type specimen book.</p>
    </section>
    <a class="button btn-gallery" href="#">VIEW GALLERY</a>

    <section class="feature-corporate">
      <h2 class="section-title"><span class="line-wide">CORPORATE</span><br><span class="line-narrow">EVENTS</span></h2>
      <p class="feature-text">Lorem Ipsum is simply dummy text of the printing and typesetting industry. Lorem Ipsum has been the industry's standard dummy text ever since the 1500s, when an unknown printer took a galley of type and scrambled it to make a type specimen book.</p>
    </section>
    <a class="button btn-events" href="#">VIEW EVENTS</a>
    <div class="photo-frame frame-corporate">
      <div class="photo photo-corporate" role="img" aria-label="Conference room with microphones and water jug on a table before a seated audience"></div>
    </div>

    <section class="info-col col-about">
      <div class="info-bar"></div>
      <h3 class="section-title">ABOUT US</h3>
      <p class="feature-text">Lorem Ipsum is simply dummy text of the printing and typesetting industry. Lorem Ipsum has been the industry's standard dummy text ever since the 1500s, when an unknown printer took a galley of type and scrambled it to make a type specimen book.ndustry's standard dummy text ever since the 1500s, when an unknown printer</p>
    </section>
    <section class="info-col col-services">
      <div class="info-bar"></div>
      <h3 class="section-title">SERVICES</h3>
      <p class="feature-text">Lorem Ipsum is simply dummy text of the printing and typesetting industry. Lorem Ipsum has been the industry's standard dummy text ever since the 1500s, when an unknown printer took a galley of type and scrambled it to make a type specimen book.ndustry's standard dummy text ever since the 1500s, when an unknown printer</p>
    </section>
    <section class="info-col col-clients">
      <div class="info-bar"></div>
      <h3 class="section-title">CLIENTS</h3>
      <p class="feature-text">Lorem Ipsum is simply dummy text of the printing and typesetting industry. Lorem Ipsum has been the industry's standard dummy text ever since the 1500s, when an unknown printer took a galley of type and scrambled it to make a type specimen book.ndustry's standard dummy text ever since the 1500s, when an unknown printer</p>
    </section>
  </main>

  <div class="footer-rule">
    <span style="background:var(--orange)"></span>
    <span style="background:var(--pink)"></span>
    <span style="background:var(--blue)"></span>
    <span style="background:var(--red)"></span>
    <span style="background:var(--lime)"></span>
    <span style="background:var(--orange)"></span>
    <span style="background:var(--pink)"></span>
    <span style="background:var(--blue)"></span>
    <span style="background:var(--red)"></span>
    <span style="background:var(--lime)"></span>
  </div>
  <footer class="site-footer">Copyright © 2013 OddBlockEvents. <a href="#">Privacy Policy</a></footer>
</div>
</body>
</html>
```